Professional business cards for real estate development company

I need business cards for my new real estate development company. The company, "KORVA" is a real estate development, investment, and advisory firm with a focus on multifamily, office, and mixed-use projects across primary and secondary markets in the Southeast United States.

Style preference is modern

Industry/Entity Type

Real Estate Development

Contact Information for Business Card

The business cards need to include:
Name
Title
Mailing Address
Phone Number
Web Address

Logo is attached. I would like white to be the primary color with incorporation of the company colors: #232D3A and #B5A451

Font styles to use
Other font styles liked:
• Montserrat, Avenir

Requirements
Must have
• Company Logo. No need to include the company name since the name is in the logo.
Should not have
• No line type designs

```html
<!DOCTYPE html>
<html lang="en">
<head>
<meta charset="utf-8">
<title>KORVA – Business Card</title>
<link rel="stylesheet" href="https://fonts.googleapis.com/css2?family=Montserrat:wght@600;700&family=Nunito+Sans:wght@400;600&display=swap">
<style>
  :root {
    --backdrop: #5570b6;
    --brand-navy: #232d3a;
    --card-white: #f3f3f1;
    --gold: #8b7417;
    --white: #ffffff;
  }
  * { margin: 0; padding: 0; box-sizing: border-box; }
  html, body {
    width: 1200px;
    height: 1200px;
    overflow: hidden;
    background: var(--backdrop);
  }
  .sheet {
    width: 1200px;
    height: 1200px;
    display: flex;
    flex-direction: column;
    align-items: center;
    justify-content: center;
    gap: 70px;
  }
  .card {
    position: relative;
    width: 840px;
    height: 480px;
    overflow: hidden;
    box-shadow: 0 18px 40px rgba(20, 30, 70, 0.35);
  }
  .wordmark {
    display: flex;
    align-items: center;
    gap: 12px;
    font-family: "Montserrat", sans-serif;
    font-weight: 600;
    letter-spacing: 0.08em;
    white-space: nowrap;
  }
  .wordmark__square { border: 3px solid currentColor; }

  /* Front */
  .card--front { background: var(--brand-navy); }
  .card--front .wordmark {
    position: absolute;
    left: 50%;
    top: 50%;
    transform: translate(-50%, -50%);
    color: var(--white);
    font-size: 54px;
  }
  .card--front .wordmark__square { width: 40px; height: 40px; }

  /* Back */
  .card--back { background: var(--card-white); color: var(--gold); }
  .card--back .wordmark {
    position: absolute;
    left: 56px;
    top: 52px;
    font-size: 34px;
  }
  .card--back .wordmark__square { width: 26px; height: 26px; border-width: 2.5px; }
  .identity {
    position: absolute;
    left: 56px;
    top: 118px;
  }
  .identity__name {
    font-family: "Montserrat", sans-serif;
    font-weight: 700;
    font-size: 32px;
    white-space: nowrap;
  }
  .identity__title {
    font-family: "Nunito Sans", sans-serif;
    font-size: 19px;
    margin-top: 4px;
  }
  .contact {
    position: absolute;
    left: 470px;
    top: 262px;
    font-family: "Nunito Sans", sans-serif;
    font-style: normal;
    font-weight: 600;
    font-size: 17px;
    line-height: 1.5;
    white-space: nowrap;
  }
  .contact__group + .contact__group { margin-top: 12px; }
</style>
</head>
<body>
<main class="sheet">

  <section class="card card--front" aria-label="Card front">
    <div class="wordmark">
      <span class="wordmark__square"></span>
      <span class="wordmark__name">KORVA</span>
    </div>
  </section>

  <section class="card card--back" aria-label="Card back">
    <div class="wordmark">
      <span class="wordmark__square"></span>
      <span class="wordmark__name">KORVA</span>
    </div>
    <div class="identity">
      <h1 class="identity__name">Mr. Daniel Hart</h1>
      <p class="identity__title">Real Estate Developer</p>
    </div>
    <address class="contact">
      <div class="contact__group">
        <p>+15550142873 | +15550198364</p>
        <p>daniel.hart@korvadevelopment.com</p>
        <p>www.korvadevelopment.com</p>
      </div>
      <div class="contact__group">
        <p>27th Floor name of dummy Bldg</p>
        <p>1234 Fill with your dummy address</p>
        <p>City Name, Southeast United States</p>
      </div>
    </address>
  </section>

</main>
</body>
</html>
```